Ashby Meadows Thank-You Tag

Looking for a file that incorporates current branding/colors and says:

"Thanks for Swimming with Us!"
Ashby Meadows Otters

Samples of other pieces we've done recently are attached.

Will be printed on cardstock that is
Width: 3.5 inches
Height: 2.5 inches

```html
<!DOCTYPE html>
<html lang="en">
<head>
<meta charset="utf-8">
<title>Ashby Meadows Otters – Thank-You Tags</title>
<link rel="stylesheet" href="https://fonts.googleapis.com/css2?family=Barlow+Condensed:ital,wght@1,800&family=Bungee&family=Montserrat:ital,wght@0,500;1,500&display=swap">
<style>
  :root {
    --board: #e1e1e1;
    --white: #ffffff;
    --pink: #ff4f98;
    --pink-deep: #d81f6e;
    --pink-soft: #f7a8cb;
    --navy: #163d95;
    --blue: #3d6fd8;
    --blue-soft: #a9c0f0;
    --slate: #6680b8;
  }
  html, body {
    margin: 0;
    width: 1200px;
    height: 992px;
    overflow: hidden;
    background: var(--board);
  }
  .board { position: relative; width: 1200px; height: 992px; }
  .tag { position: absolute; width: 461px; height: 329px; display: block; }
  .tag--pink-wave { left: 135px; top: 157px; }
  .tag--blue-wave { left: 613px; top: 159px; }
  .tag--brush { left: 135px; top: 500px; }
  .tag--panel { left: 613px; top: 500px; }

  .type-block { font-family: "Bungee", "Arial Black", sans-serif; }
  .type-italic { font-family: "Barlow Condensed", "Arial Narrow", sans-serif; font-weight: 800; font-style: italic; }
  .type-club { font-family: "Montserrat", Arial, sans-serif; font-weight: 500; }
  .type-club--italic { font-style: italic; }

  .fill-white { fill: var(--white); }
  .fill-pink { fill: var(--pink); }
  .fill-navy { fill: var(--navy); }
  .fill-slate { fill: var(--slate); }
  .rule-pink { stroke: var(--pink); stroke-width: 1.6; }
</style>
</head>
<body>
<main class="board">

  <!-- Pink wave tag -->
  <svg class="tag tag--pink-wave" viewBox="0 0 461 329" aria-label="Thank-you tag, pink wave version">
    <defs>
      <linearGradient id="pinkArtFill" x1="0" y1="0" x2="0" y2="1">
        <stop offset="0" stop-color="var(--white)"/>
        <stop offset="0.4" stop-color="var(--pink-soft)"/>
        <stop offset="1" stop-color="var(--pink-deep)"/>
      </linearGradient>
    </defs>
    <rect class="fill-white" width="461" height="329"/>
    <rect role="img" aria-label="Flowing pink wave artwork" x="0" y="204" width="461" height="125" fill="url(#pinkArtFill)"/>
    <text class="type-block fill-pink" x="45" y="74" font-size="62" textLength="376" lengthAdjust="spacingAndGlyphs">THANKS FOR</text>
    <text class="type-block fill-pink" x="23" y="113" font-size="40" textLength="386" lengthAdjust="spacingAndGlyphs">SWIMMING WITH US!</text>
    <text class="type-club fill-navy" x="149" y="151" font-size="15" textLength="169" lengthAdjust="spacingAndGlyphs">ASHBY MEADOWS</text>
    <text class="type-italic fill-navy" x="111" y="200" font-size="58" textLength="247" lengthAdjust="spacingAndGlyphs">OTTERS</text>
  </svg>

  <!-- Blue wave tag -->
  <svg class="tag tag--blue-wave" viewBox="0 0 461 329" aria-label="Thank-you tag, blue wave version">
    <defs>
      <linearGradient id="blueArtFill" x1="0" y1="0" x2="0" y2="1">
        <stop offset="0" stop-color="var(--white)"/>
        <stop offset="0.4" stop-color="var(--blue-soft)"/>
        <stop offset="1" stop-color="var(--blue)"/>
      </linearGradient>
    </defs>
    <rect class="fill-white" width="461" height="329"/>
    <rect role="img" aria-label="Flowing blue wave artwork" x="0" y="204" width="461" height="125" fill="url(#blueArtFill)"/>
    <text class="type-block fill-navy" x="45" y="74" font-size="62" textLength="376" lengthAdjust="spacingAndGlyphs">THANKS FOR</text>
    <text class="type-block fill-navy" x="23" y="113" font-size="40" textLength="386" lengthAdjust="spacingAndGlyphs">SWIMMING WITH US!</text>
    <text class="type-club fill-slate" x="149" y="151" font-size="15" textLength="169" lengthAdjust="spacingAndGlyphs">ASHBY MEADOWS</text>
    <text class="type-italic fill-slate" x="111" y="200" font-size="58" textLength="247" lengthAdjust="spacingAndGlyphs">OTTERS</text>
  </svg>

  <!-- Brush tag -->
  <svg class="tag tag--brush" viewBox="0 0 461 329" aria-label="Thank-you tag, brush version">
    <defs>
      <linearGradient id="brandBlendA" x1="0" y1="1" x2="1" y2="0">
        <stop offset="0" stop-color="var(--pink)"/>
        <stop offset="0.5" stop-color="#a24a9a"/>
        <stop offset="1" stop-color="var(--navy)"/>
      </linearGradient>
    </defs>
    <rect width="461" height="329" fill="url(#brandBlendA)"/>
    <ellipse role="img" aria-label="White brush-stroke artwork" class="fill-white" cx="226" cy="180" rx="196" ry="136"/>
    <text class="type-italic fill-navy" x="135" y="91" font-size="40" textLength="190" lengthAdjust="spacingAndGlyphs">THANKS FOR</text>
    <text class="type-italic fill-navy" x="102" y="138" font-size="56" textLength="257" lengthAdjust="spacingAndGlyphs">SWIMMING</text>
    <text class="type-italic fill-navy" x="126" y="184" font-size="56" textLength="204" lengthAdjust="spacingAndGlyphs">WITH US!</text>
    <line class="rule-pink" x1="113" y1="211" x2="154" y2="211"/>
    <text class="type-club type-club--italic fill-navy" x="160" y="217" font-size="16" textLength="143" lengthAdjust="spacingAndGlyphs">ASHBY MEADOWS</text>
    <line class="rule-pink" x1="310" y1="211" x2="351" y2="211"/>
    <text class="type-italic fill-navy" x="108" y="264" font-size="60" textLength="247" lengthAdjust="spacingAndGlyphs">OTTERS</text>
  </svg>

  <!-- Panel tag -->
  <svg class="tag tag--panel" viewBox="0 0 461 329" aria-label="Thank-you tag, panel version">
    <defs>
      <linearGradient id="brandBlendB" x1="0" y1="1" x2="1" y2="0">
        <stop offset="0" stop-color="var(--pink)"/>
        <stop offset="0.5" stop-color="#a24a9a"/>
        <stop offset="1" stop-color="var(--navy)"/>
      </linearGradient>
    </defs>
    <rect width="461" height="329" fill="url(#brandBlendB)"/>
    <path class="fill-white" d="M37 119 A103 103 0 0 1 140 16 L424 16 L424 208 A103 103 0 0 1 321 311 L37 311 Z"/>
    <text class="type-italic fill-navy" x="124" y="70" font-size="44" textLength="213" lengthAdjust="spacingAndGlyphs">THANKS FOR</text>
    <text class="type-italic fill-navy" x="87" y="122" font-size="62" textLength="288" lengthAdjust="spacingAndGlyphs">SWIMMING</text>
    <text class="type-italic fill-navy" x="115" y="176" font-size="62" textLength="227" lengthAdjust="spacingAndGlyphs">WITH US!</text>
    <line class="rule-pink" x1="98" y1="205" x2="144" y2="205"/>
    <text class="type-club type-club--italic fill-pink" x="153" y="212" font-size="18" textLength="159" lengthAdjust="spacingAndGlyphs">ASHBY MEADOWS</text>
    <line class="rule-pink" x1="319" y1="205" x2="365" y2="205"/>
    <text class="type-italic fill-pink" x="94" y="265" font-size="66" textLength="275" lengthAdjust="spacingAndGlyphs">OTTERS</text>
  </svg>

</main>
</body>
</html>
```